Design a corporate looking website for Harbourline Funding

Need design only WordPress mock up for Harbourline Funding who provides short term finance solutions to other businesses. We need a corporate looking website that depicts a trustworthy, Dynamic fast acting company.
Visit http://q7.pagemockery.net/ for current mock up We need something like e this but not the same with a design that depicts corporate with more colour and images, needs to install trust and fast action. Please feel free to change the layout as I am not wedded to current design but am happy with what on the landing page.

Target Market(s)

Small to medium sized Businesses

Industry/Entity Type

Finance

Number of Pages Required

1 page

Font styles to use
Sans Serif

Requirements
Must have
• Design Landing pages in WordPress
• Visit http://q7.pagemockery.net/ for current mock up need Layout like this but with a design that depicts corporate with more colour and images, needs to install trust and fast action. Please feel free to change the layout as I am not happy with current design but am wedded to what on the landing page.
Should not have
• any copyright material on it.

```html
<!DOCTYPE html>
<html lang="en">
<head>
<meta charset="utf-8">
<title>Harbourline Funding</title>
<link href="https://fonts.googleapis.com/css2?family=Source+Sans+3:ital,wght@0,400;0,600;0,700;1,400&display=swap" rel="stylesheet">
<style>
:root{
  --blue:#2a9ff0;
  --blue-deep:#1b6fb4;
  --hero-a:#3f8fd6;
  --hero-b:#6fb2ea;
  --grey-text:#9a9a9a;
  --grey-light:#c4c4c4;
  --grey-band:#b9b9b9;
  --icon-bg:#e4e4e4;
  --orange:#f7923e;
  --pink:#f23a9c;
  --track:#ececec;
  --footer:#ececec;
  --white:#ffffff;
}
*{box-sizing:border-box;margin:0;padding:0}
html,body{width:1200px;height:2679px;overflow:hidden;background:var(--white);font-family:"Source Sans 3",Arial,sans-serif;color:var(--grey-text)}
.page{position:relative;width:1200px;height:2679px}
.abs{position:absolute}

/* hero */
.hero{position:absolute;left:0;top:0;width:1200px;height:366px;background:linear-gradient(160deg,var(--hero-b),var(--hero-a) 60%,#2f7dc4)}
.topbar{position:absolute;left:0;top:0;width:1200px;height:54px;background:rgba(255,255,255,.28);border-bottom:1px solid rgba(255,255,255,.5)}
.brand{position:absolute;left:70px;top:16px;display:flex;align-items:center;gap:8px;font-weight:700;font-size:17px;color:#1c3f75;text-transform:uppercase}
.brand .mark{width:16px;height:16px;background:#1c3f75}
.nav{position:absolute;left:376px;top:20px;display:flex;gap:22px;font-style:italic;font-size:13px;color:#2b4f86}
.nav .active{color:#fff}
.slide-arrow{position:absolute;top:160px;width:38px;height:40px;background:rgba(255,255,255,.35);display:flex;align-items:center;justify-content:center}
.hero-card{position:absolute;left:711px;top:107px;width:382px;height:250px;background:var(--white);border:10px solid #1d1d1d;border-radius:8px 8px 0 0;padding:30px 24px 0}
.hero-card h1{font-size:18px;line-height:1.3;color:var(--blue);text-transform:uppercase;text-align:center;font-weight:700}
.hero-card p{font-size:11.5px;line-height:1.45;color:#6c6c6c;margin-top:10px}
.btn-start{display:block;margin:14px auto 0;width:112px;height:34px;background:var(--blue);color:#fff;font-size:15px;line-height:34px;text-align:center}

/* services */
.section-title{position:absolute;left:0;width:1200px;text-align:center}
.section-title h2{font-size:22px;font-weight:700;color:var(--grey-light);text-transform:uppercase;letter-spacing:.5px}
.section-title p{font-size:15px;color:var(--blue);margin-top:2px}
.service{position:absolute;width:300px;text-align:center}
.service .icon{width:88px;height:88px;border-radius:50%;background:var(--icon-bg);margin:0 auto;display:flex;align-items:center;justify-content:center}
.service h3{margin-top:18px;font-size:16px;line-height:1.3;font-weight:700;color:var(--grey-light);text-transform:uppercase}
.service p{margin:6px auto 0;width:220px;font-size:12.5px;line-height:1.4;color:var(--grey-text)}
.more{display:inline-block;margin-top:12px;width:116px;height:32px;background:#f2f2f2;box-shadow:2px 2px 3px rgba(0,0,0,.18);font-size:12px;font-style:italic;color:var(--grey-light);line-height:32px}
.more b{color:var(--blue);font-style:normal}

/* why band */
.why-band{position:absolute;left:0;top:1541px;width:1200px;height:61px;background:var(--grey-band);color:#fff;text-align:center;padding-top:8px}
.why-band h2{font-size:16px;font-weight:700;text-transform:uppercase}
.why-band p{font-size:15px}

.h-blue{font-size:16px;font-weight:700;color:var(--blue);text-transform:uppercase}
.h-orange{font-size:16px;font-weight:700;color:var(--orange);text-transform:uppercase}
.about-media{position:absolute;left:80px;top:1666px;width:447px;height:272px;background:radial-gradient(circle at 55% 45%,#d9dde2,#8a929b 70%,#5b636c)}
.why-text{position:absolute;left:586px;top:1694px;width:520px;font-size:10.5px;line-height:1.5;font-style:italic;color:#d0d0d0}
.pill{position:absolute;top:1898px;height:40px;color:#fff;font-weight:700;font-size:13px;display:flex;align-items:center;text-transform:uppercase}
.pill .ic{width:36px;height:40px;border-right:1px solid rgba(255,255,255,.5);display:flex;align-items:center;justify-content:center}
.pill span{padding-left:10px}

.step-num{position:absolute;top:2006px;font-size:26px;color:#9a9a9a}
.track{position:absolute;top:2082px;width:268px;height:30px;background:var(--track)}
.track i{display:block;height:100%;background:var(--orange)}

.start{position:absolute;left:109px;top:2182px;width:109px;height:40px;background:var(--pink);color:#fff;display:flex;align-items:center;font-size:15px}
.start .ic{width:36px;height:40px;border-right:1px solid rgba(255,255,255,.5);display:flex;align-items:center;justify-content:center}
.start span{padding-left:12px}

.sub-h{font-size:14px;font-style:italic;color:#8a8a8a}
.faq{position:absolute;left:570px;font-size:12px;font-style:italic;color:#b5b5b5;display:flex;align-items:center;gap:14px}
.faq i{width:14px;height:14px;border:1px solid #bbb;display:block}

.footer{position:absolute;left:0;top:2438px;width:1200px;height:241px;background:var(--footer);box-shadow:0 -4px 8px rgba(0,0,0,.12) inset}
.fcol{position:absolute;top:36px;font-size:14.5px;line-height:1.9;color:#a8a8a8}
.fcol h4{font-size:15px;font-style:italic;font-weight:400;color:#8a8a8a;margin-bottom:2px}
.social{position:absolute;top:2632px;width:32px;height:32px;border-radius:50%;background:var(--orange)}
</style>
</head>
<body>
<div class="page">

  <header class="hero">
    <div class="hero-photo abs" role="img" aria-label="Photo of a city street with parked bicycles, tinted blue" style="inset:0;background:linear-gradient(180deg,rgba(40,100,60,.25),rgba(60,130,200,.1) 55%,rgba(180,190,200,.25))"></div>
    <div class="topbar">
      <div class="brand"><i class="mark"></i>Harbourline Funding</div>
      <nav class="nav">
        <span class="active">Home</span><span>Services</span><span>Why Harbourline</span><span>Investors</span><span>About Us</span><span>Contact Us</span><span>Members Login</span>
      </nav>
    </div>
    <div class="slide-arrow" style="left:0"><svg width="26" height="26" viewBox="0 0 26 26"><circle cx="13" cy="13" r="12" fill="none" stroke="#fff" stroke-width="2"/><path d="M15 7l-6 6 6 6" fill="none" stroke="#fff" stroke-width="3"/></svg></div>
    <div class="slide-arrow" style="right:0"><svg width="26" height="26" viewBox="0 0 26 26"><circle cx="13" cy="13" r="12" fill="none" stroke="#fff" stroke-width="2"/><path d="M15 7l-6 6 6 6" fill="none" stroke="#fff" stroke-width="3"/></svg></div>
    <div class="hero-card">
      <h1>Commission assistance providing commission advance when you need it,</h1>
      <p>ever since the 1500s, when an unknown printer took a galley of type and scrambled it to make a type specimen book.</p>
      <span class="btn-start">Get Start</span>
    </div>
  </header>

  <div class="section-title" style="top:398px">
    <h2>Our Services</h2>
    <p>We can do all this for you.</p>
  </div>

  <!-- service grid -->
  <div class="service" style="left:198px;top:465px">
    <div class="icon"><svg width="50" height="50" viewBox="0 0 50 50"><path d="M25 8l13 11v12H12V19z" fill="var(--blue)"/><rect x="22" y="22" width="6" height="9" fill="#e4e4e4"/><path d="M4 32c6 0 10 8 21 8s15-8 21-8v6c-6 0-10 8-21 8S10 38 4 38z" fill="var(--blue)"/></svg></div>
    <h3>Residental Read<br>Estate Agents</h3>
    <p>Radable English. Many desktop publishing packages and web page editors now use Lorem Ipsum as</p>
    <span class="more">Find out more <b>»</b></span>
  </div>
  <div class="service" style="left:707px;top:465px">
    <div class="icon"><svg width="50" height="50" viewBox="0 0 50 50"><circle cx="22" cy="28" r="16" fill="none" stroke="var(--blue)" stroke-width="3"/><path d="M6 28h32M22 12v32M10 18h24M10 38h24" stroke="var(--blue)" stroke-width="2.5"/><circle cx="36" cy="12" r="7" fill="var(--blue)"/><circle cx="36" cy="12" r="2.5" fill="#e4e4e4"/></svg></div>
    <h3>Motor Vehicle &amp; Earth<br>Moving Equipment</h3>
    <p>readable content of a page when looking at its layout. The point of using Lorem Ipsum is that it has a</p>
    <span class="more">Find out more <b>»</b></span>
  </div>
  <div class="service" style="left:198px;top:742px">
    <div class="icon"><svg width="50" height="50" viewBox="0 0 50 50"><g fill="var(--blue)"><rect x="8" y="10" width="20" height="6" rx="3"/><rect x="8" y="18" width="20" height="6" rx="3"/><rect x="8" y="26" width="20" height="6" rx="3"/><rect x="8" y="34" width="20" height="6" rx="3"/></g><circle cx="33" cy="32" r="12" fill="var(--blue)" stroke="#e4e4e4" stroke-width="2"/><text x="33" y="38" font-size="16" font-weight="700" text-anchor="middle" fill="#fff" font-family="Arial,sans-serif">$</text></svg></div>
    <h3>Commercial Read<br>Estate Agents</h3>
    <p>or randomised words which don't look even slightly believable. If you are going to use a passage of</p>
    <span class="more">Find out more <b>»</b></span>
  </div>
  <div class="service" style="left:707px;top:742px">
    <div class="icon"><svg width="50" height="50" viewBox="0 0 50 50"><path d="M23 9a17 17 0 1 0 17 19H23z" fill="var(--blue)"/><path d="M27 5v19h18A18 18 0 0 0 27 5z" fill="var(--blue)"/></svg></div>
    <h3>Mortgage &amp; Finance<br>Brokers</h3>
    <p>sentence structures, to generate Lorem Ipsum which looks reasonable. The generated Lorem Ipsum is</p>
    <span class="more">Find out more <b>»</b></span>
  </div>
  <div class="service" style="left:198px;top:1006px">
    <div class="icon"><svg width="50" height="50" viewBox="0 0 50 50"><circle cx="25" cy="25" r="21" fill="none" stroke="var(--blue)" stroke-width="2.5"/><path d="M14 14l22 22M36 14L14 36" stroke="var(--blue)" stroke-width="5"/></svg></div>
    <h3>Financial<br>Planners</h3>
    <p>reproduced below for those interested. Sections 1.10.32 and 1.10.33 from "de Finibus Bonorum et</p>
    <span class="more">Find out more <b>»</b></span>
  </div>
  <div class="service" style="left:707px;top:1006px">
    <div class="icon"><svg width="50" height="50" viewBox="0 0 50 50"><path d="M10 12c4-5 10-3 13-1 3-2 9-4 13 1 3 4 1 10-1 15-2 6-2 14-5 14s-3-10-7-10-4 10-7 10-3-8-5-14c-2-5-4-11-1-15z" fill="var(--blue)"/><circle cx="32" cy="26" r="6" fill="#e4e4e4" stroke="var(--blue)" stroke-width="2"/><path d="M36 30l6 6" stroke="var(--blue)" stroke-width="3"/></svg></div>
    <h3>Medical and Dental<br>Equipment</h3>
    <p>that are extremely painful. Nor again is there anyone who loves or pursues or desires to obtain pain</p>
    <span class="more">Find out more <b>»</b></span>
  </div>
  <div class="service" style="left:198px;top:1269px">
    <div class="icon"><svg width="50" height="50" viewBox="0 0 50 50"><ellipse cx="25" cy="25" rx="20" ry="14" transform="rotate(-40 25 25)" fill="var(--blue)"/><path d="M14 34l22-18" stroke="#e4e4e4" stroke-width="2"/></svg></div>
    <h3>Office Equipment and<br>Technology Agents</h3>
    <p>enjoy a pleasure that has no annoying consequences, or one who avoids pain that produces no</p>
    <span class="more">Find out more <b>»</b></span>
  </div>
  <div class="service" style="left:707px;top:1269px">
    <div class="icon"><svg width="50" height="50" viewBox="0 0 50 50"><circle cx="25" cy="20" r="4" fill="var(--blue)"/><path d="M17 12a11 11 0 0 0 0 16M33 12a11 11 0 0 1 0 16M12 7a18 18 0 0 0 0 26M38 7a18 18 0 0 1 0 26" fill="none" stroke="var(--blue)" stroke-width="2.5"/><path d="M25 22l-8 24M25 22l8 24M20 38h10" stroke="var(--blue)" stroke-width="2.5"/></svg></div>
    <h3>Telecommunications</h3>
    <p style="margin-top:42px">easy to distinguish. In a free hour, when our power of choice is untrammelled and when nothing prevents</p>
    <span class="more">Find out more <b>»</b></span>
  </div>

  <section class="why-band">
    <h2>Why Harbourline</h2>
    <p>Find more about us and what makes us different</p>
  </section>

  <h2 class="h-blue abs" style="left:80px;top:1636px">About Our Business</h2>
  <div class="about-media" role="img" aria-label="Photo of hands using a tablet with floating squares and a play button">
    <svg class="abs" style="left:193px;top:106px" width="60" height="60" viewBox="0 0 60 60"><circle cx="30" cy="30" r="26" fill="none" stroke="#7a1f3a" stroke-width="3"/><path d="M24 18l18 12-18 12z" fill="#7a1f3a"/></svg>
  </div>

  <h2 class="h-orange abs" style="left:586px;top:1660px">Why Harbourline Funding</h2>
  <p class="why-text">At Harbourline Funding our aim is to provide immediate commission advance solutions for all industries. Our background is sales, property and finance and we understand the issues faced with small to medium businesses, agents, contractors and consultants who earn commissions. Unforeseen expenses, increased sales, holiday periods, sickness, taxation bills and job changes can all have an effect on a sales and commission flow. Harbourline Funding is here to help if you have outstanding commissions that could be used now, then we may have an answer. Once approved you will have an advance on your outstanding commission within hours, giving you the cash flow to keep moving.</p>
  <div class="pill" style="left:589px;width:215px;background:var(--blue)"><div class="ic"><svg width="14" height="14"><rect x="1" y="1" width="12" height="12" fill="none" stroke="#fff" stroke-width="1.5"/></svg></div><span>Our Pricing Guarantee</span></div>
  <div class="pill" style="left:825px;width:214px;background:var(--pink)"><div class="ic"><svg width="14" height="14"><circle cx="7" cy="4" r="3" fill="#fff"/><path d="M1 14c0-5 12-5 12 0z" fill="#fff"/></svg></div><span>Our Loyalty Program</span></div>

  <h2 class="abs" style="left:80px;top:1956px;font-size:16px;font-weight:700;color:#9a9a9a;text-transform:uppercase">3 Easy Steps to a Stress Solution</h2>
  <div class="step-num" style="left:109px;color:var(--pink)">1</div>
  <div class="step-num" style="left:471px">2</div>
  <div class="step-num" style="left:827px">3</div>
  <div class="abs" style="left:109px;top:2044px;font-size:14px;font-style:italic;color:#c8c8c8">Call or Click</div>
  <div class="track" style="left:109px"><i style="width:120px"></i></div>
  <div class="track" style="left:471px"><i style="width:202px"></i></div>
  <div class="track" style="left:827px"><i style="width:255px"></i></div>
  <div class="abs" style="left:109px;top:2122px;font-size:15px;font-style:italic;color:#8a8a8a">A hassle free finance solution that grows as your business grows</div>
  <div class="start"><div class="ic"><svg width="14" height="14"><path d="M2 1l11 6-11 6z" fill="#fff"/></svg></div><span>Start</span></div>

  <div class="sub-h abs" style="left:120px;top:2268px">What people say About us</div>
  <p class="abs" style="left:118px;top:2304px;width:430px;font-size:11.5px;font-style:italic;color:#c4c4c4;line-height:1.5">The service was beyond my expectations. But please, replace this with an actual customer testimonial, this is just for testing purposes.</p>
  <div class="abs" style="left:118px;top:2366px;font-size:14px;display:flex;align-items:center;gap:10px"><svg width="16" height="14"><rect x="1" y="4" width="14" height="9" fill="none" stroke="#777" stroke-width="1.5"/><path d="M5 4V1h6v3" fill="none" stroke="#777" stroke-width="1.5"/></svg><span style="color:var(--orange);font-style:italic;font-weight:600">Marcus Hale</span><span style="color:#8a8a8a">, Hale Events</span></div>

  <div class="sub-h abs" style="left:607px;top:2266px">Frequently Asked Quesions</div>
  <div class="faq" style="top:2312px"><i></i>How long does it take?</div>
  <div class="faq" style="top:2344px"><i></i>What are the conditions?</div>
  <div class="faq" style="top:2376px"><i></i>What documents do i need?</div>

  <footer class="footer">
    <div class="fcol" style="left:143px"><h4>About Us</h4>Home<br>Services<br>Why Harbourline</div>
    <div class="fcol" style="left:375px"><h4>Harbourline Funding</h4>Investors<br>Consultant<br>Testimonials</div>
    <div class="fcol" style="left:634px"><h4>Members Login</h4>Client login<br>Consultant login<br>investor login</div>
    <div class="fcol" style="left:862px"><h4>Contact Details</h4>4th Place holder street<br>Harbour City ZIP code<br>Tel: 1234</div>
  </footer>
  <div class="social" style="left:989px"></div>
  <div class="social" style="left:1030px"></div>
  <div class="social" style="left:1071px"></div>
  <div class="social" style="left:1112px"></div>
</div>
</body>
</html>
```